Business Card Re-Design...or logo does not look sharp

Hello

We are a start-up and just need someone to help us.

Our colors are: Delilah charm pink (yeah I know) and charcoal for the lettering.

I am attaching our logo which needs cleaning up.

We want the JUST the lady ironing on the table (pink) in front, and the background in charcoal. All the business info can be on the back.

Dims on card are 2 x 2''

Also, if you have better ideas....please let us know!

Thanks

Marcus

Business

Casa Brisa Dorada
4821 Pelham Ridge Dr Suite B2
El Paso TX 79958
915-555-0143

```html
<!DOCTYPE html>
<html lang="en">
<head>
<meta charset="utf-8">
<title>Casa Brisa Dorada – Business Card Font Options</title>
<link rel="stylesheet" href="https://fonts.googleapis.com/css2?family=Parisienne&family=Grand+Hotel&family=Great+Vibes&family=Questrial&display=swap">
<style>
  :root {
    --canvas-grey: #c9c9c9;
    --card-pink: #cfb0b2;
    --card-pink-light: #dcc2c4;
    --card-pink-edge: #b89a9c;
    --charcoal: #1b1718;
    --band-text: #e6dcdd;
    --label-white: #ffffff;
  }
  * { box-sizing: border-box; margin: 0; padding: 0; }
  html, body {
    width: 1200px;
    height: 1000px;
    overflow: hidden;
    background: var(--canvas-grey);
  }
  .presentation {
    position: relative;
    width: 1200px;
    height: 1000px;
  }
  .font-label {
    position: absolute;
    font-family: "Questrial", "Century Gothic", sans-serif;
    font-size: 54px;
    color: var(--label-white);
    line-height: 1;
    white-space: nowrap;
  }
  .font-label--aspire { left: 710px; top: 80px; }
  .font-label--grand-hotel { left: 148px; top: 443px; }
  .font-label--great-vibes { left: 706px; top: 898px; }

  .card {
    position: absolute;
    width: 649px;
    height: 379px;
    overflow: hidden;
    box-shadow: 2px 3px 6px rgba(0,0,0,0.45);
  }
  .card--aspire { left: 33px; top: 38px; z-index: 1; }
  .card--grand-hotel { left: 510px; top: 370px; z-index: 2; }
  .card--great-vibes { left: 35px; top: 590px; z-index: 3; }

  .card__pattern {
    position: absolute;
    inset: 0;
    background:
      radial-gradient(ellipse at 50% 60%, var(--card-pink-light) 0%, var(--card-pink) 60%, var(--card-pink-edge) 100%);
  }
  .card__name {
    position: absolute;
    left: 0;
    right: 0;
    text-align: center;
    color: var(--charcoal);
    white-space: nowrap;
    line-height: 1;
  }
  .card--aspire .card__name {
    font-family: "Parisienne", cursive;
    font-size: 66px;
    top: 48px;
  }
  .card--grand-hotel .card__name {
    font-family: "Grand Hotel", cursive;
    font-size: 74px;
    top: 40px;
  }
  .card--great-vibes .card__name {
    font-family: "Great Vibes", cursive;
    font-size: 70px;
    top: 44px;
  }
  .card__address-band {
    position: absolute;
    left: 0;
    right: 0;
    top: 132px;
    height: 31px;
    background: var(--charcoal);
    color: var(--band-text);
    font-family: "Questrial", "Century Gothic", sans-serif;
    font-size: 21px;
    line-height: 31px;
    text-align: center;
    white-space: nowrap;
  }
  .card--grand-hotel .card__address-band { top: 145px; }
  .card--great-vibes .card__address-band { top: 133px; }
  .card__phone {
    position: absolute;
    right: 36px;
    bottom: 42px;
    display: flex;
    align-items: center;
    gap: 6px;
    font-family: "Questrial", "Century Gothic", sans-serif;
    font-size: 31px;
    color: var(--charcoal);
    line-height: 1;
  }
  .card__phone-icon { width: 44px; height: 30px; display: block; }
</style>
</head>
<body>
<main class="presentation">

  <section class="card card--aspire">
    <div class="card__pattern" role="img" aria-label="Soft pink damask pattern background"></div>
    <div class="card__name">Casa Brisa Dorada</div>
    <div class="card__address-band">4821 Pelham Ridge Dr&nbsp; | &nbsp;Suite B2&nbsp; | &nbsp;El Paso, TX 79958</div>
    <div class="card__phone">
      <svg class="card__phone-icon" viewBox="0 0 44 30" aria-hidden="true">
        <path d="M3 11 C3 3 41 3 41 11 L41 14 L31 14 L31 10 L13 10 L13 14 L3 14 Z" fill="currentColor"/>
        <path d="M10 14 L34 14 L39 28 L5 28 Z" fill="currentColor"/>
        <circle cx="22" cy="20" r="4" fill="#cfb0b2"/>
      </svg>
      <span>915-555-0143</span>
    </div>
  </section>

  <section class="card card--grand-hotel">
    <div class="card__pattern" role="img" aria-label="Soft pink damask pattern background"></div>
    <div class="card__name">Casa Brisa Dorada</div>
    <div class="card__address-band">4821 Pelham Ridge Dr&nbsp; | &nbsp;Suite B2&nbsp; | &nbsp;El Paso, TX 79958</div>
    <div class="card__phone">
      <svg class="card__phone-icon" viewBox="0 0 44 30" aria-hidden="true">
        <path d="M3 11 C3 3 41 3 41 11 L41 14 L31 14 L31 10 L13 10 L13 14 L3 14 Z" fill="currentColor"/>
        <path d="M10 14 L34 14 L39 28 L5 28 Z" fill="currentColor"/>
        <circle cx="22" cy="20" r="4" fill="#cfb0b2"/>
      </svg>
      <span>915-555-0143</span>
    </div>
  </section>

  <section class="card card--great-vibes">
    <div class="card__pattern" role="img" aria-label="Soft pink damask pattern background"></div>
    <div class="card__name">Casa Brisa Dorada</div>
    <div class="card__address-band">4821 Pelham Ridge Dr&nbsp; | &nbsp;Suite B2&nbsp; | &nbsp;El Paso, TX 79958</div>
    <div class="card__phone">
      <svg class="card__phone-icon" viewBox="0 0 44 30" aria-hidden="true">
        <path d="M3 11 C3 3 41 3 41 11 L41 14 L31 14 L31 10 L13 10 L13 14 L3 14 Z" fill="currentColor"/>
        <path d="M10 14 L34 14 L39 28 L5 28 Z" fill="currentColor"/>
        <circle cx="22" cy="20" r="4" fill="#cfb0b2"/>
      </svg>
      <span>915-555-0143</span>
    </div>
  </section>

  <div class="font-label font-label--aspire">Aspire</div>
  <div class="font-label font-label--grand-hotel">Grand Hotel</div>
  <div class="font-label font-label--great-vibes">Great Vibes</div>

</main>
</body>
</html>
```